Business Cards that are elegant and wow

I want to create and print business cards that represent my brand and stand out from the rest. We want to ensure they stay in our branding and the integrity is not lost. I am happy to look at different shapes like square etc.

It will be printed on very thick cards and will be stylish .

I want to create and print business cards that represent my brand and stand out from the rest. We want to ensure they stay in ur branding and the integrity is not lost. I am happy to look at different shapes like square etc.

Target Market(s)

real estate professionals

Industry/Entity Type

Real Estate

Contact Information for Business Card

Maren Holt
hello@brightfernrealty.com.au
brightfernrealty.com.au
0487 316 252 (SMS)

Colors

Designer to choose colors to be used in the design.

Requirements
Must have
• My logo
• email
• website
• Name
Nice to have
• I like the idea of printing with foil or spot gloss. You want it to stand out in a sea.
Should not have
• I would like you to stay in my colour themes. Don't change the colour of my logo

```html
<!DOCTYPE html>
<html lang="en">
<head>
<meta charset="utf-8">
<title>Bright Fern Realty – Business Card</title>
<link rel="stylesheet" href="https://fonts.googleapis.com/css2?family=Roboto:wght@300&family=Source+Sans+3:wght@400;600;700&display=swap">
<style>
  :root {
    --brand-cyan: #00aeef;
    --brand-pink: #ec1a7b;
    --ink: #444444;
    --label: #4a4a4a;
    --tagline: #8a8a8a;
    --rule: #cfcfcf;
    --card-edge: #dddddd;
    --city-light: #f4f4f4;
    --city-mid: #d6d6d6;
    --city-dark: #b4b4b4;
    --page: #ffffff;
  }
  * { box-sizing: border-box; margin: 0; padding: 0; }
  html, body {
    width: 1200px; height: 1054px; overflow: hidden;
    background: var(--page);
    font-family: "Source Sans 3", "Myriad Pro", sans-serif;
  }
  .sheet { position: relative; width: 1200px; height: 1054px; }
  .side-label {
    position: absolute; top: 34px; width: 518px;
    text-align: center; font-weight: 700; font-size: 27px; color: var(--label);
  }
  .side-label--front { left: 71px; }
  .side-label--back { left: 613px; }

  .card {
    position: absolute; top: 91px; width: 518px; height: 906px;
    background: #fff; overflow: hidden;
  }
  .card--front { left: 71px; border: 1px solid var(--card-edge); }
  .card--back { left: 613px; }

  .brand {
    position: absolute; left: 0; right: 0;
    display: flex; align-items: center; justify-content: center; gap: 14px;
    font-family: "Source Sans 3", sans-serif; font-weight: 600;
    font-size: 36px; letter-spacing: 1px; text-transform: uppercase; white-space: nowrap;
  }
  .brand__dot {
    width: 58px; height: 58px; border-radius: 50%;
    border: 6px solid currentColor; flex: none;
  }
  .card--front .brand { top: 130px; color: var(--brand-cyan); }
  .card--back .brand { top: 86px; color: #fff; z-index: 2; }

  .divider {
    position: absolute; top: 231px; left: 26px; right: 24px;
    height: 1px; background: var(--rule);
  }
  .tagline {
    position: absolute; top: 236px; left: 0; right: 0; text-align: center;
    font-family: "Roboto", sans-serif; font-weight: 300; font-size: 26px;
    color: var(--tagline); word-spacing: 2px;
  }
  .tagline__sep { margin: 0 12px; }

  .back-band { position: absolute; top: 0; left: 0; width: 518px; height: 310px; }

  .contact {
    position: absolute; top: 364px; left: 0; right: 0;
    text-align: center; color: var(--ink); font-size: 26px; line-height: 45px;
  }
  .contact__name { font-weight: 700; font-size: 27px; }

  .cityscape {
    position: absolute; left: 0; right: 0; bottom: 0; height: 264px;
    background: linear-gradient(to bottom, var(--city-light) 0%, var(--city-mid) 55%, var(--city-light) 88%, var(--city-dark) 94%, var(--city-dark) 100%);
  }
</style>
</head>
<body>
<main class="sheet">
  <h2 class="side-label side-label--front">Front</h2>
  <h2 class="side-label side-label--back">Back</h2>

  <section class="card card--front" aria-label="Card front">
    <div class="brand"><span class="brand__dot"></span><span>Bright Fern Realty</span></div>
    <div class="divider"></div>
    <p class="tagline">Trust<span class="tagline__sep">•</span>Value<span class="tagline__sep">•</span>Relationships</p>
    <div class="cityscape" role="img" aria-label="Grey line illustration of a city street with office towers, houses and trees"></div>
  </section>

  <section class="card card--back" aria-label="Card back">
    <svg class="back-band" viewBox="0 0 518 310" aria-hidden="true">
      <polygon points="0,0 518,0 518,207 0,305" fill="var(--brand-pink)"/>
      <polygon points="0,0 518,0 518,195 0,294" fill="var(--brand-cyan)"/>
    </svg>
    <div class="brand"><span class="brand__dot"></span><span>Bright Fern Realty</span></div>
    <div class="contact">
      <p class="contact__name">Maren Holt</p>
      <p>hello@brightfernrealty.com.au</p>
      <p>brightfernrealty.com.au</p>
      <p>0487 316 252 (SMS)</p>
    </div>
    <div class="cityscape" role="img" aria-label="Grey line illustration of a city street with office towers, houses and trees"></div>
  </section>
</main>
</body>
</html>
```